Website Page Re-Design

I have 2 pages that need to be re-designed on my site. This is the site so you can take a look and get a feel for the layout etc, www.vortaplay.com
I have included screen shots of the individual pages I want redone as well as some examples from other sites for ideas.

Homepage Story, would like the redo sunday file, to be made stunning, only the content, picture and share buttons need be altered the, would like and emphasis on intergrating the share buttons, the story page starts here http://www.vortaplay.com/league/ball-hockey/mens/news-division/ so what is beingcreated is when the read more is clicked

Free Agent Forms:
Needs to be re-worked so that there isn't so much white space on the page.

Industry/Entity Type

News

Requirements
Must have
• share buttons to slick very well intergrated
Nice to have
• Share buttons to be top notch

```html
<!DOCTYPE html>
<html lang="en">
<head>
<meta charset="utf-8">
<title>VortaPlay Sports – News</title>
<link rel="stylesheet" href="https://fonts.googleapis.com/css2?family=Source+Sans+3:ital,wght@0,400;0,600;1,400;1,600&display=swap">
<style>
:root{
  --bg-green:#7fb241;
  --bg-green-light:#9ccb5f;
  --panel:#e4f0d4;
  --panel-edge:#c9dfae;
  --banner-top:#9fcb63;
  --banner-bottom:#5f9a2a;
  --tab-yellow:#fbe77a;
  --tab-divider:#8a7a2a;
  --ink:#111;
  --body-grey:#7a7a7a;
  --meta-grey:#555;
  --accent-green:#6a9a2c;
  --white:#fff;
  --logo-cream:#fff4c2;
}
*{box-sizing:border-box;margin:0;padding:0}
html,body{width:1200px;height:810px;overflow:hidden}
body{
  position:relative;
  font-family:"Source Sans 3",sans-serif;
  background:radial-gradient(ellipse at 50% 20%,var(--bg-green-light) 0%,var(--bg-green) 60%,#74a636 100%);
}
.brand{
  position:absolute;left:134px;top:24px;
  font-size:44px;font-weight:600;color:var(--logo-cream);letter-spacing:-0.5px;
}
.utility-nav{
  position:absolute;left:656px;top:0;width:413px;height:26px;
  background:var(--tab-yellow);border-radius:0 0 8px 8px;
  display:flex;align-items:center;list-style:none;padding-left:12px;
}
.utility-nav li{font-size:15px;font-weight:600;color:var(--ink);padding:0 14px;border-left:1px solid var(--tab-divider);line-height:20px}
.utility-nav li:first-child{border-left:0;padding-left:16px;padding-right:22px}
.main-nav{
  position:absolute;left:511px;top:39px;width:558px;height:50px;
  background:#111;border-radius:6px 14px 10px 18px;
  display:flex;align-items:center;list-style:none;padding-left:30px;
}
.main-nav li{font-size:15.5px;font-style:italic;color:var(--white);text-decoration:underline;padding:0 12px;border-left:1px solid #777;line-height:16px}
.main-nav li:first-child{border-left:0}
.page-panel{
  position:absolute;left:135px;top:103px;width:938px;height:619px;
  background:var(--panel);border-radius:8px;box-shadow:0 2px 3px rgba(0,0,0,.18);
}
.banner{
  position:absolute;left:12px;top:13px;width:908px;height:108px;
  background:linear-gradient(var(--banner-top),var(--banner-bottom));border-radius:3px;overflow:hidden;
}
.banner-players{
  position:absolute;left:18px;top:0;width:632px;height:108px;
  background:linear-gradient(90deg,#c9b7a0,#d8c3ae 40%,#b8a592 70%,#cfc5b8);opacity:.85;
}
.follow-button{
  position:absolute;left:696px;top:23px;width:164px;height:63px;background:#000;border-radius:6px;
  display:flex;align-items:center;padding-left:16px;gap:12px;color:var(--white);
  font-size:16px;font-style:italic;line-height:16px;
}
.follow-button .square{width:33px;height:33px;border-radius:4px;background:#5b79b0}
.content-card{
  position:absolute;left:13px;top:136px;width:903px;height:460px;background:var(--white);border-radius:8px;
}
.section-title{position:absolute;left:30px;top:30px;font-size:28px;font-weight:400;color:var(--ink)}
.post{position:absolute;left:30px;top:80px;width:480px}
.post-title{font-size:22px;font-weight:400;color:var(--accent-green);margin-bottom:6px}
.post p{font-size:13.5px;line-height:22.5px;color:var(--body-grey)}
.post p + p{margin-top:10px}
.post-meta{margin-top:10px;font-size:13.5px;font-weight:600;color:var(--meta-grey);padding-left:2px}
.share-bar{display:flex;gap:10px;margin-top:14px;padding-left:2px}
.share{display:flex;align-items:center;height:19px;font-size:11.5px}
.share .btn{display:flex;align-items:center;gap:4px;height:19px;padding:0 5px;border:1px solid #c2c8d6;background:linear-gradient(#f6f7fa,#dde2ec);border-radius:2px;font-weight:600;color:#333}
.share .btn i{width:11px;height:11px;border-radius:2px;display:block}
.share .count{margin-left:3px;height:19px;padding:0 4px;line-height:17px;border:1px solid #c2c8d6;background:#fff;border-radius:2px;color:#333}
.share.plus .btn i{background:#4f8ee8}
.share.like .btn i{background:#3b5998}
.share.chirp .btn i{background:#33aadd}
.share.send .btn{background:#f05a3a;border-color:#d64b2e;color:#fff}
.share.send .btn i{background:#fff}
.share.send .count{font-weight:600}
.post-photo{
  position:absolute;left:525px;top:79px;width:360px;height:275px;
  background:linear-gradient(#2a5bb5 0%,#3a64b4 30%,#ddd8d2 45%,#eeeae6 75%,#4f8d3a 92%,#3c7a2c 100%);
}
.copyright{position:absolute;left:141px;top:744px;font-size:11px;letter-spacing:1px;color:var(--white)}
</style>
</head>
<body>
  <div class="brand">VortaPlay Sports</div>

  <ul class="utility-nav">
    <li>Home</li><li>About Us</li><li>FAQS</li><li>Contact Us</li><li>Jobs</li>
  </ul>

  <ul class="main-nav">
    <li>Leagues</li><li>Schedules &amp; More</li><li>Register</li><li>Pay</li><li>Forum</li><li>Sponsors</li>
  </ul>

  <main class="page-panel">
    <div class="banner">
      <div class="banner-players" role="img" aria-label="Row of league players in team jerseys and helmets"></div>
      <div class="follow-button"><span class="square"></span><span>Find Us On<br>Chatterly</span></div>
    </div>

    <section class="content-card">
      <h1 class="section-title">Recent Blog Post/ News</h1>
      <article class="post">
        <h2 class="post-title">Mauris vel lacus vitae felis vestibulum</h2>
        <p>Vivamus porttitor, g, purus nisi eleifend libero, a tempus libero lectus feugiat felis. Morbi diam mauris, viverra in, gravida eu, mattis in, ante. Morbi eget arcu.<br>Morbi porta, libero id ullamcorper nonummy, nibh ligula pulvinar metus, eget consect-etuer augue nisi quis lacus. Ut ac mi quis lacus mollis aliquam. Curabitur iaculis tempus eros. Curabitur vel mi sit amet magna malesuada ultrices</p>
        <p>Mauris neque metus, malesuada nec, ultricies sit amet, porttitor mattis, enim. In massa libero, interdum nec, interdum vel, blandit sed, nulla. In ullamcorper, est eget tempor cursus, neque mi consectetuer mi, a ultricies massa est sed nisl. Class aptent taciti sociosqu ad litora torquent per conubia nostra, per inceptos</p>
        <div class="post-meta">Posted on 20 Sep 2013 &nbsp;|&nbsp; Comments</div>
        <div class="share-bar">
          <div class="share like"><span class="btn"><i></i>Like</span><span class="count">3k</span></div>
          <div class="share chirp"><span class="btn"><i></i>Chirp</span><span class="count">316</span></div>
          <div class="share plus"><span class="btn"><i></i>+1</span><span class="count">56</span></div>
          <div class="share send"><span class="btn"><i></i>Share</span><span class="count">4.6K</span></div>
        </div>
      </article>
      <div class="post-photo" role="img" aria-label="Team photo of players in Rinks for Roofs shirts holding a large donation cheque in a gym"></div>
    </section>
  </main>

  <footer class="copyright">© 2011, VORTAPLAY SPORTS. ALL RIGHTS RESERVED.</footer>
</body>
</html>
```